Awesome Web Design Project

must have a link to mingleton of the homepage preferably a scrolling view of our mingleton page!

We are an exciting new electrical company with a strong focus on energy efficiency and offering the latest technologies.

The design should allow easy navigation, there shouldn't be too many menus, It should look clean and sleek, Colours to consider could be green, silver/chrome, black,

The site should convey technology, efficiency and simplicity

Must be viewable on all devices, pc's, tablets, phones ie Responsive
Updates

Logo and some pics uploaded!

Industry/Entity Type

Electrical

Requirements
Must have
• must include the following pages,
about us
our services
gallery
contact us
Connect with us
Nice to have
• Would be great if the website design used a user friendly cms,
Should not have
• too many links, menus, clutter it should be clean and easy to navigate

```html
<!DOCTYPE html>
<html lang="en">
<head>
<meta charset="utf-8">
<title>Volter Electrical</title>
<link rel="stylesheet" href="https://fonts.googleapis.com/css2?family=Open+Sans:wght@400;600;700&family=Noto+Serif&display=swap">
<style>
:root{
  --frame-dark:#1f1e33;
  --frame-light:#e4e6ea;
  --footer:#363450;
  --footer-deep:#2a2940;
  --field:#25243a;
  --white:#ffffff;
  --text-grey:#7b7d86;
  --blue-top:#3b6fc4;
  --blue-bottom:#1c4a98;
  --accent-green:#b6d431;
  --rule:#d2d4d9;
  --footer-text:#a7a6bd;
}
*{margin:0;padding:0;box-sizing:border-box}
html,body{width:1200px;height:1000px;overflow:hidden;background:var(--white)}
body{position:relative;font-family:"Open Sans",Arial,sans-serif}
.abs{position:absolute}
.frame{left:199px;top:0;width:790px;height:1000px;
  background:linear-gradient(var(--frame-dark) 0,#34334b 90px,#6f7084 190px,#c4c6cd 280px,#dfe1e5 400px,var(--frame-light) 793px)}
.footer{left:199px;top:793px;width:790px;height:207px;
  background:radial-gradient(ellipse at 50% 30%,#45435f 0,var(--footer) 45%,var(--footer-deep) 100%)}
.logo{left:302px;top:58px;display:flex;align-items:center;gap:7px;color:var(--accent-green);font-weight:700;font-size:12.5px;letter-spacing:.6px;white-space:nowrap}
.logo-mark{width:18px;height:18px;background:var(--accent-green)}
.nav-item{top:60px;font-size:9.5px;line-height:15px;color:var(--white);white-space:nowrap}
.nav-item.current{background:#dcdde2;color:#222;border-radius:3px;font-weight:600;padding:0 6px}
.hero-title{left:342px;top:134px;color:var(--white);font-size:19px;font-weight:400}
.hero-copy{left:342px;top:171px;color:var(--white);font-size:9.3px;font-weight:600;line-height:11.6px;white-space:nowrap}
.btn{display:flex;align-items:center;justify-content:center;color:var(--white);font-weight:600;border-radius:3px;
  background:linear-gradient(var(--blue-top),var(--blue-bottom));box-shadow:0 1px 2px rgba(0,0,0,.35);white-space:nowrap}
.hero-btn{left:371px;top:247px;width:104px;height:24px;font-size:12px}
.btn-shadow{left:373px;top:288px;width:100px;height:8px;border-radius:50%;background:radial-gradient(rgba(60,60,70,.45),transparent 70%)}
.arrow{width:22px;height:22px}
.hero-photo{left:510px;top:103px;width:326px;height:184px;border:3px solid #f2f2f2;box-shadow:0 0 14px rgba(255,255,255,.7);
  background:linear-gradient(#8a5a48 0,#9b6a55 60%,#6c4a33 80%,#7a5638 100%)}
.card{top:314px;width:138px;height:89px;background:linear-gradient(#fbfbfc,#dcdde1);border:1px solid #fff;border-radius:3px;box-shadow:0 0 3px rgba(0,0,0,.25)}
.card-label{position:absolute;font-size:9.5px;color:var(--text-grey);line-height:30px}
.card-photo{position:absolute;top:3px;width:75px;height:82px;border-radius:3px;border:1px solid #999}
.quote{left:390px;top:429px;width:400px;text-align:center;font-family:"Noto Serif",Georgia,serif;font-size:8.6px;line-height:15px;color:var(--text-grey);white-space:nowrap}
.quote b{font-weight:400;color:#5b6f8f}
.section-title{left:400px;top:487px;width:394px;text-align:center;font-size:13.5px;font-weight:400;color:#3a3c44}
.section-sub{left:480px;top:503px;font-size:7.5px;color:#3d5a99}
.feature-photo{left:334px;top:527px;width:174px;height:130px;background:linear-gradient(#b8bcc4,#5f6670 45%,#3a3f46)}
.bullets{left:575px;top:536px;list-style:none;font-size:7.2px;color:var(--text-grey);white-space:nowrap}
.bullets li,.rows li{display:flex;align-items:center;gap:7px}
.bullets li{height:17px}
.dot{width:6px;height:6px;border-radius:50%;background:#c8cad0;flex:none}
.btn-sm{top:636px;width:75px;height:19px;font-size:9.5px}
.rows{left:318px;top:680px;width:469px;list-style:none;font-size:7.2px;color:var(--text-grey);white-space:nowrap}
.rows li{height:20.3px;border-top:1px solid var(--rule);padding-left:3px}
.social-circle{border-radius:50%;background:#d7d8de;border:1px solid #9fa0ab}
.quote-foot{left:378px;top:803px;width:450px;font-size:7px;line-height:15px;color:var(--footer-text)}
.quote-sign{left:700px;top:828px;width:123px;text-align:right;font-size:7.5px;color:#d6d5e4;white-space:nowrap}
.footer-rule{left:328px;top:843px;width:545px;height:1px;background:rgba(255,255,255,.08)}
.foot-head{top:851px;font-size:12px;font-weight:400;color:var(--white)}
.foot-copy{left:328px;top:872px;width:210px;font-size:7px;line-height:12px;color:var(--footer-text)}
.field{background:var(--field);border:1px solid #4d4b68;border-radius:3px;box-shadow:inset 0 1px 3px rgba(0,0,0,.5)}
.field-text{font-size:7px;color:#5f5e78;padding-left:8px;line-height:13px;white-space:nowrap}
.pill{background:#f2f2f4;color:#333;font-size:7.5px;border-radius:3px;display:flex;align-items:center;justify-content:center}
.net{width:22px;height:22px;border-radius:50%;background:#4a4864}
.legal{left:480px;top:946px;font-size:7px;color:#d8d7e4}
</style>
</head>
<body>
<div class="abs frame"></div>
<div class="abs footer"></div>

<header>
  <div class="abs logo"><span class="logo-mark"></span>VOLTER ELECTRICAL</div>
  <nav>
    <span class="abs nav-item" style="left:507px">Home</span>
    <span class="abs nav-item current" style="left:540px">About us</span>
    <span class="abs nav-item" style="left:600px">Our services</span>
    <span class="abs nav-item" style="left:667px">Gallery</span>
    <span class="abs nav-item" style="left:710px">Connect with us</span>
  </nav>
</header>

<section class="hero">
  <svg class="abs arrow" style="left:307px;top:187px" viewBox="0 0 22 22"><circle cx="11" cy="11" r="11" fill="#3c3c48"/><path d="M13 6 7 11l6 5z" fill="#cfd0d6"/></svg>
  <h1 class="abs hero-title">Lorem Ipsum</h1>
  <p class="abs hero-copy">Lorem Ipsum is simply dummy<br>text of the printing and<br>typesetting industry.<br>Lorem Ipsum has been<br>the industry's standard dummy<br>text ever sinc</p>
  <div class="abs btn hero-btn">Read More</div>
  <div class="abs btn-shadow"></div>
  <div class="abs hero-photo" role="img" aria-label="Living room with wall-mounted TV and speakers in front of a brick wall"></div>
  <svg class="abs arrow" style="left:850px;top:187px" viewBox="0 0 22 22"><circle cx="11" cy="11" r="11" fill="#3c3c48"/><path d="M9 6l6 5-6 5z" fill="#cfd0d6"/></svg>
</section>

<section class="showcase">
  <div class="abs card" style="left:303px"><span class="card-label" style="left:12px;top:16px">Lorem<br>Ipsum</span><div class="card-photo" role="img" aria-label="Kitchen with blue LED strip lighting" style="left:58px;background:linear-gradient(#5a5a66,#2d2d3a 60%,#2340a8)"></div></div>
  <div class="abs card" style="left:451px"><div class="card-photo" role="img" aria-label="Open switchboard cabinet" style="left:12px;background:linear-gradient(90deg,#cfd0d4,#a9abb1 50%,#d6d7da)"></div><span class="card-label" style="left:92px;top:12px">Lorem<br>Ipsum</span></div>
  <div class="abs card" style="left:597px"><span class="card-label" style="left:13px;top:12px">Lorem<br>Ipsum</span><div class="card-photo" role="img" aria-label="Skylight ceiling with warm lighting" style="left:52px;background:linear-gradient(#6e5a3e,#c9a85c 50%,#5a4a38)"></div></div>
  <div class="abs card" style="left:744px"><span class="card-label" style="left:15px;top:11px">Lorem<br>Ipsum</span><div class="card-photo" role="img" aria-label="Library room with ceiling light" style="left:54px;width:76px;background:linear-gradient(90deg,#5a4a3e,#d8dbe0 50%,#bfc3c9)"></div>
    <svg style="position:absolute;right:-1px;top:-1px" width="32" height="32" viewBox="0 0 32 32"><path d="M6 0h26v26z" fill="#54c820"/><text x="21" y="12" transform="rotate(45 21 12)" font-size="7" font-family="Open Sans,sans-serif" font-weight="700" fill="#d8242a" text-anchor="middle">New</text></svg></div>
</section>

<svg class="abs" style="left:394px;top:436px" width="16" height="16" viewBox="0 0 16 16"><path d="M14 2 3 8l11 6" stroke="#c7c9cf" stroke-width="1.5" fill="none"/></svg>
<p class="abs quote">Lorem Ipsum is simply dummy text of the printing and typesetting industry.<br>Lorem <b>Ipsum has been the industry's</b> standard dummy text</p>
<svg class="abs" style="left:771px;top:436px" width="16" height="16" viewBox="0 0 16 16"><path d="M2 2l11 6-11 6" stroke="#c7c9cf" stroke-width="1.5" fill="none"/></svg>

<section class="feature">
  <h2 class="abs section-title">There are many variations of passages</h2>
  <p class="abs section-sub">Lorem Ipsum is simply dummy</p>
  <div class="abs feature-photo" role="img" aria-label="Office interior with modern angular ceiling lights"></div>
  <ul class="abs bullets">
    <li><span class="dot"></span>Lorem Ipsum is simply dummy text of the printing and typesetting</li>
    <li><span class="dot"></span>Industry. Lorem Ipsum has been the industry's standard</li>
    <li><span class="dot"></span>Dummy text ever since the 1500s, when an unknown printer</li>
    <li><span class="dot"></span>Took a galley of type and scrambled it to make a type specimen book.</li>
    <li><span class="dot"></span>It has survived not only five centuries, but also the</li>
  </ul>
  <div class="abs btn btn-sm" style="left:591px">Read More</div>
  <div class="abs btn btn-sm" style="left:681px">Download</div>
  <ul class="abs rows">
    <li><span class="dot"></span>Lorem Ipsum is simply dummy text of the printing and typesetting Industry. Lorem Ipsum has been the industry's standard</li>
    <li><span class="dot"></span>Dummy text ever since the 1500s, when an unknown printer Took a galley of type and scrambled it to make a type specimen book.</li>
    <li><span class="dot"></span>It has survived not only five centuries, but also the</li>
    <li><span class="dot"></span>Lorem Ipsum is simply dummy text of the printing and typesetting Industry. Lorem Ipsum has been the industry's standard</li>
    <li><span class="dot"></span>Dummy text ever since the 1500s, when an unknown printer Took a galley of type and scrambled it to make a type specimen book.</li>
  </ul>
</section>

<footer>
  <div class="abs social-circle" style="left:332px;top:804px;width:29px;height:29px" aria-label="mingleton"></div>
  <p class="abs quote-foot">Lorem Ipsum is simply dummy text of the printing and typesetting industry. Lorem Ipsum has been the industry's standard dummy text of the printing and typesetting industry.</p>
  <p class="abs quote-sign">- versions of Lorem Ipsum.</p>
  <div class="abs footer-rule"></div>

  <h3 class="abs foot-head" style="left:328px">Newsletter</h3>
  <p class="abs foot-copy">Lorem Ipsum is simply dummy text of the printing and typesetting industry. Lorem Ipsum has been the industry's</p>
  <div class="abs field field-text" style="left:328px;top:906px;width:122px;height:15px">enter your email address</div>
  <div class="abs pill" style="left:459px;top:906px;width:49px;height:15px">Subscribe</div>
  <div class="abs net" style="left:325px;top:932px"></div>
  <div class="abs net" style="left:356px;top:932px"></div>
  <div class="abs net" style="left:388px;top:932px"></div>

  <h3 class="abs foot-head" style="left:633px">Contact form</h3>
  <div class="abs field" style="left:633px;top:872px;width:123px;height:15px"></div>
  <div class="abs field" style="left:633px;top:894px;width:123px;height:15px"></div>
  <div class="abs field" style="left:633px;top:917px;width:123px;height:15px"></div>
  <div class="abs field" style="left:762px;top:872px;width:111px;height:61px"></div>
  <div class="abs pill" style="left:822px;top:943px;width:49px;height:15px">Submit</div>

  <p class="abs legal">Valid HTML5 and CSS3.</p>
</footer>
</body>
</html>
```